Business card design needed

I need a business card design for a new online retail business based in Australia. I am unsure of the exact content of what I will be selling but it will be probably women's clothing, accessories, gym wear, gifts and maybe homeware linen. I am wanting a classy design that portrays the image of class/style/upmarket.

Target Market(s)

predominantely women - 20-50 age group

Industry/Entity Type

Retail

Contact Information for Business Card

Purely Radiant
Harriet Quenby
Director
ABN 73214508836
17 Parrish Lane Kelvin Ridge NSW 2291
ph: +61 417 935 284
sales@purelyradiant.com.au

Logo Text

I am open for suggestions here

Requirements
Must have
• The design must be both sides of the card

```html
<!DOCTYPE html>
<html lang="en">
<head>
<meta charset="utf-8">
<title>Purely Radiant – Business Card</title>
<link rel="stylesheet" href="https://fonts.googleapis.com/css2?family=Roboto:wght@300;400&display=swap">
<style>
  :root {
    --orange: #f0892f;
    --rose: #d0686b;
    --purple: #a2408f;
    --ink: #555555;
    --white: #ffffff;
    --backdrop: #1a1a1a;
  }
  * { box-sizing: border-box; margin: 0; padding: 0; }
  html, body {
    width: 1200px; height: 900px; overflow: hidden;
    background: var(--backdrop);
    font-family: "Roboto", Arial, sans-serif;
  }
  .canvas {
    width: 1200px; height: 900px;
    display: flex; flex-direction: column; align-items: center; justify-content: center;
    gap: 40px;
  }
  .card {
    position: relative;
    width: 700px; height: 400px;
    background: var(--white);
    overflow: hidden;
  }
  .card-front .sweep { position: absolute; inset: 0; }
  .front-brand {
    position: absolute; left: 0; right: 0; top: 170px;
    display: flex; align-items: center; justify-content: center; gap: 14px;
  }
  .brand-dot {
    width: 26px; height: 26px; border-radius: 50%;
    background: var(--orange);
  }
  .brand-name {
    font-size: 42px; font-weight: 300; color: var(--purple);
    letter-spacing: 1px;
  }
  .card-back .side-strip {
    position: absolute; left: 0; top: 0; bottom: 0; width: 210px;
    background: linear-gradient(to bottom, var(--orange) 0%, var(--rose) 40%, var(--purple) 85%);
  }
  .strip-brand {
    position: absolute; left: 0; right: 0; bottom: 34px;
    display: flex; align-items: center; justify-content: center; gap: 8px;
  }
  .strip-brand .brand-dot { width: 12px; height: 12px; background: var(--white); }
  .strip-brand .brand-name { font-size: 20px; color: var(--white); letter-spacing: 0.5px; }
  .contact {
    position: absolute; left: 250px; top: 70px; right: 30px;
    color: var(--ink); font-weight: 300;
  }
  .person-name { font-size: 24px; font-weight: 400; color: var(--purple); }
  .person-role { font-size: 15px; margin-top: 6px; }
  .address { font-size: 15px; line-height: 1.45; margin-top: 70px; }
  .reach { margin-top: 24px; font-size: 15px; line-height: 1.6; }
  .reach-line { display: flex; align-items: center; gap: 10px; }
  .reach-line svg { width: 13px; height: 13px; fill: var(--purple); flex: none; }
</style>
</head>
<body>
<main class="canvas">
  <section class="card card-front" aria-label="Business card front">
    <svg class="sweep" viewBox="0 0 700 400" preserveAspectRatio="none" aria-hidden="true">
      <defs>
        <linearGradient id="sweep-fill" x1="0" y1="1" x2="1" y2="0">
          <stop offset="0" stop-color="#c85f78"/>
          <stop offset="0.35" stop-color="#f0892f"/>
          <stop offset="0.7" stop-color="#d0686b"/>
          <stop offset="1" stop-color="#a2408f"/>
        </linearGradient>
      </defs>
      <rect width="700" height="400" fill="url(#sweep-fill)"/>
      <ellipse cx="330" cy="160" rx="385" ry="300" fill="#ffffff"/>
    </svg>
    <div class="front-brand">
      <span class="brand-dot"></span>
      <span class="brand-name">Purely Radiant</span>
    </div>
  </section>

  <section class="card card-back" aria-label="Business card back">
    <div class="side-strip">
      <div class="strip-brand">
        <span class="brand-dot"></span>
        <span class="brand-name">Purely Radiant</span>
      </div>
    </div>
    <div class="contact">
      <p class="person-name">Harriet Quenby</p>
      <p class="person-role">Director</p>
      <p class="address">ABN 73214508836 17 Parrish Lane<br>Kelvin Ridge NSW 2291</p>
      <div class="reach">
        <p class="reach-line">
          <svg viewBox="0 0 24 24" aria-hidden="true"><path d="M6.6 10.8a15.1 15.1 0 0 0 6.6 6.6l2.2-2.2a1 1 0 0 1 1-.25 11.4 11.4 0 0 0 3.6.57 1 1 0 0 1 1 1V20a1 1 0 0 1-1 1A17 17 0 0 1 3 4a1 1 0 0 1 1-1h3.5a1 1 0 0 1 1 1c0 1.25.2 2.45.57 3.57a1 1 0 0 1-.25 1z"/></svg>
          +61 417 935 284
        </p>
        <p class="reach-line">
          <svg viewBox="0 0 24 24" aria-hidden="true"><path d="M2 5h20v14H2z M3.5 6.5 12 13l8.5-6.5" fill="none" stroke="#a2408f" stroke-width="2"/></svg>
          sales@purelyradiant.com.au
        </p>
      </div>
    </div>
  </section>
</main>
</body>
</html>
```